Tallow HVAC Services - High end letter head, Quote Template & Invoice Template

Provide word documents for the below.
- Letterhead for emails & letters.
- Quote template (similar to the attached)
- Invoice template (similar to the attached)
Logo colours should be used.
Modern, bold, professional look.
Tallow Logo - Veskor Specialist Dealer logo - Contact information

See attachments of previously used documents.

Target Market(s)

High end clients

Industry/Entity Type

Air Conditioning & Mechanical Ventilation (HVAC)

Font styles to use
Sans Serif
Other font styles liked:
• Arial Narrow or similar - Text similar to the TALLOW logo

Requirements
Must have
• Tallow Logo - Veskor Specialist Dealer logo - Contact information
Nice to have
• Logo colours used throughout the documents
Should not have
• Bright colours, yellow, pink, green etc

```html
<!DOCTYPE html>
<html lang="en">
<head>
<meta charset="utf-8">
<title>Tallow HVAC Services – Stationery Set</title>
<link rel="stylesheet" href="https://fonts.googleapis.com/css2?family=Arimo:wght@400;700&display=swap">
<style>
  :root{
    --backdrop:#e6e7e9;
    --paper:#ffffff;
    --ink:#1a1a1a;
    --brand-blue:#1ea0e0;
    --brand-navy:#1d4f9c;
    --rule-grey:#6d6e71;
    --tagline:#4a4a4a;
    --watermark:#e4e6f5;
  }
  *{margin:0;padding:0;box-sizing:border-box}
  html,body{width:1200px;height:571px;overflow:hidden;background:var(--backdrop)}
  body{position:relative;font-family:"Arimo",Arial,sans-serif;color:var(--ink)}
  .sheet{position:absolute;top:46px;width:339px;height:479px;background:var(--paper);
    box-shadow:4px 5px 8px rgba(0,0,0,.18)}
  .sheet--letterhead{left:46px}
  .sheet--quote{left:431px}
  .sheet--invoice{left:815px}
  .sheet-label{position:absolute;top:548px;width:339px;text-align:center;font-size:6.5px;font-weight:700}

  .brand{position:absolute;display:flex;align-items:center;gap:5px}
  .brand__dot{width:18px;height:18px;border-radius:50%;background:var(--brand-navy)}
  .brand__name{font-weight:700;font-size:12px;letter-spacing:.2px;color:var(--ink);line-height:1}
  .tagline{position:absolute;font-size:5.2px;letter-spacing:.4px;color:var(--tagline);white-space:nowrap}
  .tagline span{color:var(--brand-blue)}
  .rule-top{position:absolute;left:12.6px;width:303px;height:1px;background:var(--brand-blue)}
  .rule-bottom{position:absolute;height:1px;background:var(--rule-grey)}

  .partner{position:absolute;right:23px;top:13px;text-align:right;line-height:1}
  .partner__name{font-weight:700;font-size:12px;color:var(--brand-blue)}
  .partner__sub{font-size:3.6px;letter-spacing:.5px;font-weight:700;color:var(--ink);margin-top:1px}

  .contact{position:absolute;font-size:6.4px;line-height:9.6px;white-space:nowrap}
  .contact .sep{color:var(--brand-blue)}
  .contact svg{width:5px;height:5px;vertical-align:-0.5px;fill:var(--brand-blue);margin:0 1px 0 4px}
  .contact--centered{text-align:center;left:0;width:339px}
  .contact__company{font-weight:700;font-size:6.4px}

  .watermark{position:absolute;left:110px;top:290px;width:245px;height:170px}
</style>
</head>
<body>

<!-- Letterhead -->
<section class="sheet sheet--letterhead">
  <div class="brand" style="left:12.6px;top:13px">
    <div class="brand__dot"></div>
    <div class="brand__name">TALLOW HVAC SERVICES</div>
  </div>
  <div class="tagline" style="left:12.6px;top:38px"><span>|</span> HEATING <span>|</span> VENTILATION <span>|</span> AIR CONDITIONING <span>|</span></div>
  <div class="rule-top" style="top:50px"></div>

  <svg class="watermark" role="img" aria-label="Faint brand mark decoration" viewBox="0 0 245 170">
    <defs><radialGradient id="wm" cx=".6" cy=".5" r=".5">
      <stop offset="0" stop-color="#eef0fa"/><stop offset="1" stop-color="#ffffff"/></radialGradient></defs>
    <circle cx="150" cy="85" r="80" fill="url(#wm)"/>
  </svg>

  <div class="rule-bottom" style="left:12.6px;width:313px;top:440px"></div>
  <div class="contact" style="left:12.6px;top:449px">
    PO Box 12 Kelsby, NSW 2299<svg viewBox="0 0 10 10"><rect x="2" y="0" width="6" height="10" rx="1"/></svg>0400 555 018<svg viewBox="0 0 10 10"><rect x="0" y="1.5" width="10" height="7"/></svg>tom@tallowhvac.com.au<svg viewBox="0 0 10 10"><circle cx="5" cy="5" r="5"/></svg>www.tallowhvac.com.au<br>
    ABN: 51 604 227 309 <span class="sep">|</span> Licence No: 218845C <span class="sep">|</span> ARC No: AU60217
  </div>
</section>
<div class="sheet-label" style="left:46px">Tallow-LH-template</div>

<!-- Quote -->
<section class="sheet sheet--quote">
  <div class="brand" style="left:12px;top:12px">
    <div class="brand__dot"></div>
    <div class="brand__name">TALLOW HVAC SERVICES</div>
  </div>
  <div class="partner">
    <div class="partner__name">VESKOR</div>
    <div class="partner__sub">SPECIALIST DEALER</div>
  </div>
  <div class="rule-top" style="top:39.5px;left:12px"></div>

  <div class="rule-bottom" style="left:12px;width:314px;top:439px"></div>
  <div class="contact" style="left:12px;top:448px">
    PO Box 12 Kelsby, NSW 2299<svg viewBox="0 0 10 10"><rect x="2" y="0" width="6" height="10" rx="1"/></svg>0400 555 018<svg viewBox="0 0 10 10"><rect x="0" y="1.5" width="10" height="7"/></svg>tom@tallowhvac.com.au<svg viewBox="0 0 10 10"><circle cx="5" cy="5" r="5"/></svg>www.tallowhvac.com.au<br>
    ABN: 51 604 227 309 <span class="sep">|</span> Licence No: 218845C <span class="sep">|</span> ARC No: AU60217
  </div>
</section>
<div class="sheet-label" style="left:431px">New Quote Template</div>

<!-- Invoice -->
<section class="sheet sheet--invoice">
  <div class="brand" style="left:90px;top:13px">
    <div class="brand__dot"></div>
    <div class="brand__name">TALLOW HVAC SERVICES</div>
  </div>
  <div class="tagline" style="left:90px;top:38px"><span>|</span> HEATING <span>|</span> VENTILATION <span>|</span> AIR CONDITIONING <span>|</span></div>
  <div class="rule-top" style="top:50px"></div>

  <div class="rule-bottom" style="left:12.6px;width:303px;top:430px"></div>
  <div class="contact contact--centered" style="top:438px">
    <div class="contact__company">TALLOW HVAC SERVICES PTY LTD</div>
    PO Box 12 Kelsby, NSW 2299<svg viewBox="0 0 10 10"><rect x="2" y="0" width="6" height="10" rx="1"/></svg>0400 555 018<svg viewBox="0 0 10 10"><rect x="0" y="1.5" width="10" height="7"/></svg>tom@tallowhvac.com.au<svg viewBox="0 0 10 10"><circle cx="5" cy="5" r="5"/></svg>www.tallowhvac.com.au<br>
    ABN: 51 604 227 309 <span class="sep">|</span> Licence No: 218845C <span class="sep">|</span> ARC No: AU60217
  </div>
</section>
<div class="sheet-label" style="left:815px">New Invoice Template.</div>

</body>
</html>
```